Letterhead & Business Card for our Professional Practice (Financial Services)

We are looking for someone to design a letterhead and business card for our business, which is a professional practice called Harbor Lumen Capital Limited. The website is at www.harborrlumencapital.example.co.uk.

The letterhead needs to have: (a) our logo (b) address (c) telephone number (d) email address and (e) our company number.

We would like the stationary to be consistent with the website.

I have attached the logo in EPS and PNG format.

Target Market(s)

Professional services, large commercial enterprises, financial services

Industry/Entity Type

Financial Service

Font styles to use
Serif

Colors
3176b5
f04a50

Requirements
Must have
• Be consistent with our website located at www.harborlumencapital.example.co.uk
• Be in the following formats:
• 1. Word template for the letterhead
• 2. PDF for the letterhead with setup and bleeds required at www.presskite.example.co.uk
• 3. PDF for the business card with setup and bleeds required at www.presskite.example.co.uk
Nice to have
• Something with a really interesting design that says "these guys are professional but dynamic and interesting"
Should not have
• Boring

```html
<!DOCTYPE html>
<html lang="en">
<head>
<meta charset="utf-8">
<title>Harbor Lumen Capital – Stationery</title>
<link rel="stylesheet" href="https://fonts.googleapis.com/css2?family=Cuprum:wght@700&family=PT+Sans&family=Jost:wght@400&display=swap">
<style>
:root{
  --navy:#003d6e;
  --red:#c8192e;
  --paper:#f5f4f2;
  --white:#ffffff;
  --ink:#2b2b2b;
  --backdrop:#a9a8a9;
  --brand-font:"Cuprum",sans-serif;
  --body-font:"PT Sans",sans-serif;
  --contact-font:"Jost",sans-serif;
}
*{box-sizing:border-box;margin:0;padding:0}
html,body{width:1123px;height:1200px;overflow:hidden;background:var(--backdrop)}
.canvas{position:relative;width:1123px;height:1200px}
.sheet{position:absolute;box-shadow:0 2px 8px rgba(0,0,0,.35)}
.brand{font-family:var(--brand-font);font-weight:700;color:var(--navy);white-space:nowrap;display:flex;align-items:center;gap:6px}
.brand-mark{display:inline-block;background:var(--red)}
.band{position:absolute;left:0;right:0;bottom:0;background:var(--navy)}
.band::after{content:"";position:absolute;top:0;bottom:0;right:0;width:19%;background:var(--red);clip-path:polygon(6% 0,100% 0,100% 100%,0 100%)}

/* letterhead */
.letterhead{left:62px;top:34px;width:509px;height:718px;background:var(--paper)}
.letterhead .brand{position:absolute;left:0;right:0;top:80px;justify-content:center;font-size:17px}
.letterhead .brand-mark{width:10px;height:10px}
.letter{position:absolute;left:54px;top:200px;width:410px;font-family:var(--body-font);color:var(--ink)}
.letter .greeting{font-size:13px;color:#555;margin-bottom:20px}
.letter p{font-size:6.9px;line-height:12.3px;text-align:justify;margin-bottom:12.3px;color:#333}
.letter .closing{margin-top:24px;font-size:7px}
.signature{display:block;width:70px;height:26px;margin:8px 0 9px -2px;background:linear-gradient(90deg,#d9d8d6,#c9c8c6)}
.letter .signer{font-size:8px;line-height:13px;color:#444;padding-left:3px}
.letter-footer{position:absolute;left:0;right:0;top:675px;text-align:center;font-family:var(--contact-font);font-size:8px;line-height:11px;color:#111}
.letter-footer b{font-weight:400;color:var(--navy)}
.letterhead .band{height:12px}

/* cover */
.cover{left:588px;top:34px;width:509px;height:718px;background:var(--navy);display:flex;align-items:center;justify-content:center}
.cover .brand{color:var(--white);font-size:26px;gap:12px}
.cover .brand-mark{width:22px;height:22px}

/* envelopes */
.envelope-back{left:144px;top:770px;width:572px;height:260px;background:var(--paper)}
.envelope-flap{position:absolute;left:0;top:0}
.envelope-back .brand{position:absolute;left:0;right:0;top:38px;justify-content:center;color:var(--white);font-size:14px}
.envelope-back .brand-mark{width:9px;height:9px}
.envelope-front{left:73px;top:885px;width:573px;height:261px;background:var(--paper)}
.envelope-front .sender{position:absolute;left:18px;top:22px;text-align:center}
.envelope-front .brand{font-size:17px;justify-content:center}
.envelope-front .brand-mark{width:10px;height:10px}
.envelope-front address{font-style:normal;font-family:var(--contact-font);font-size:8.5px;line-height:10px;color:#111;margin-top:4px}
.envelope-front .band{height:12px}

/* business cards */
.card-front{left:791px;top:806px;width:222px;height:126px;background:var(--white)}
.card-front .brand{position:absolute;left:10px;top:66px;font-size:11.5px;gap:4px}
.card-front .brand-mark{width:7px;height:7px}
.card-divider{position:absolute;left:114px;top:28px;width:1px;height:58px;background:#d6d6d6}
.card-details{position:absolute;left:126px;top:24px;font-family:var(--contact-font);color:#111;font-size:5.6px;line-height:7px}
.card-details .name{font-size:7.5px;line-height:9px;color:var(--navy);text-transform:uppercase}
.card-details .role{color:var(--red);margin-bottom:3px}
.card-details .line{display:flex;align-items:center;gap:3px}
.card-details svg{width:5px;height:5px;fill:var(--navy)}
.card-front .band{height:8px}
.card-back{left:791px;top:964px;width:222px;height:127px;background:var(--navy)}
.card-back .brand{position:absolute;left:0;right:0;top:52px;justify-content:center;color:var(--white);font-size:12px;gap:5px}
.card-back .brand-mark{width:7px;height:7px}
.card-back .web{position:absolute;left:0;right:0;top:110px;text-align:center;font-family:var(--contact-font);font-size:5.6px;letter-spacing:1.2px;color:var(--white)}
</style>
</head>
<body>
<div class="canvas">

  <section class="sheet letterhead">
    <div class="brand"><span class="brand-mark"></span>Harbor Lumen Capital</div>
    <div class="letter">
      <p class="greeting">Dear Mr. Keller,</p>
      <p>Lorem ipsum dolor sit amet, consectetur adipiscing elit. Donec orci purus, luctus vitae dignissim eu, iaculis sed purus. Vivamus faucibus, ipsum nec aliquet viverra, leo mauris condimentum ligula, sit amet sagittis enim ligula quis arcu. Nam egestas tortor id nisi porttitor mattis. In tortor ante, ultricies in suscipit a, tempus non massa. Vivamus et auctor mi. Fusce vel massa nulla. Phasellus nec eros mauris, et scelerisque orci.</p>
      <p>Donec malesuada orci vitae nulla accumsan porta a id massa. Quisque accumsan iaculis magna sit amet fringilla. Maecenas consequat, magna eget tincidunt semper, odio nibh rutrum mi, id feugiat ante nisi eu risus. Vestibulum nunc orci, rhoncus a placerat in, ultricies in mi. Cras mattis varius eros, vel fringilla nisi suscipit eget. Quisque scelerisque sagittis nulla at porttitor.</p>
      <p>Sed id augue vitae urna euismod commodo aliquet a quam. Pellentesque arcu velit, cursus et malesuada ut, consequat et diam. Nullam erat sem, rhoncus id ullamcorper vitae, rhoncus et arcu. In ultricies ultricies nulla, ut rutrum nisi iaculis at. Donec eu magna a metus ornare faucibus. Fusce aliquet faucibus ultricies. Morbi semper, est id tincidunt gravida, sem arcu adipiscing lacus, ac bibendum nulla leo eu purus. Quisque nec diam sed risus consectetur a accumsan quis quis nibh. Vestibulum id purus lorem.</p>
      <p>It is a long established fact that a reader will be distracted by the readable content of a page when looking at its layout. The point of using Lorem Ipsum is that it has a more-or-less normal distribution of letters, as opposed to using 'Content here, content here', making it look like readable English. Many desktop publishing packages</p>
      <p class="closing">Sincerely,</p>
      <span class="signature" role="img" aria-label="Handwritten signature"></span>
      <p class="signer">Martin Keller<br>CEO/ Founder</p>
    </div>
    <div class="letter-footer">
      412 Juniper Row, Harbor Point, Alaska 34590<br>
      <b>P:</b> 555 014 2290 &nbsp;<b>E:</b> name@mailhost.example &nbsp;<b>W:</b> harborrlumencapital.example.co.uk
    </div>
    <div class="band"></div>
  </section>

  <section class="sheet cover">
    <div class="brand"><span class="brand-mark"></span>Harbor Lumen Capital</div>
  </section>

  <section class="sheet envelope-back">
    <svg class="envelope-flap" width="572" height="96" viewBox="0 0 572 96" aria-hidden="true">
      <path d="M0 0H572L558 60Q552 94 520 94H52Q20 94 14 60Z" fill="var(--navy)"/>
    </svg>
    <div class="brand"><span class="brand-mark"></span>Harbor Lumen Capital</div>
  </section>

  <section class="sheet envelope-front">
    <div class="sender">
      <div class="brand"><span class="brand-mark"></span>Harbor Lumen Capital</div>
      <address>412 Juniper Row, Harbor Point<br>Alaska 34590</address>
    </div>
    <div class="band"></div>
  </section>

  <section class="sheet card-front">
    <div class="brand"><span class="brand-mark"></span>Harbor Lumen Capital</div>
    <div class="card-divider"></div>
    <div class="card-details">
      <div class="name">Martin Keller</div>
      <div class="role">CEO/Founder</div>
      <div>412 Juniper Row</div>
      <div>Harbor Point, Alaska 34590</div>
      <div class="line"><svg viewBox="0 0 10 10"><path d="M2 0l2 2-1 2q1 2 3 3l1-1 2 2-1 2Q3 10 0 2z"/></svg>555 014 2290</div>
      <div class="line"><svg viewBox="0 0 10 10"><path d="M0 2h10v6H0zM0 2l5 3 5-3"/></svg>name@mailhost.example</div>
      <div class="line"><svg viewBox="0 0 10 10"><circle cx="5" cy="5" r="5"/></svg>harborrlumencapital.example.co.uk</div>
    </div>
    <div class="band"></div>
  </section>

  <section class="sheet card-back">
    <div class="brand"><span class="brand-mark"></span>Harbor Lumen Capital</div>
    <div class="web">www.harborrlumencapital.example.co.uk</div>
  </section>

</div>
</body>
</html>
```